Business Card/Documentation - Rebranding
Stonevia - Civil & Geo-Technical Construction
Business Card/Documentation - Rebranding - Engineering
Creative Brief
Simple
Example Name
Manager
C/248 Kelting Ridge Rd, Marrow Vale North, 2081, NSW
T +61 2 9735 2194
info@stonevia.com.au
stonevia.com.au
We would like you to show design creativity in reducing the amount of text. As an example we are happy to not show a fax number, or website as it may be seen as redundant (due to email address). We would also like the designs in PSD format so that we can add employee details in as required. (Hence the generic information)
Specialising in.... Landslip & Flood Remediation Earth Retaining Structures Embankment Stabilisation Road & Drainage Repairs Bridge Reconstruction Rockfall Protection Marine & Foreshore Erosion Control Landfill Construction & Rehabilitation (Again happy to leave this to suggestion)

```html
<!DOCTYPE html>
<html lang="en">
<head>
<meta charset="utf-8">
<title>Stonevia – Stationery Concepts</title>
<link href="https://fonts.googleapis.com/css2?family=Open+Sans:wght@400;600;700&family=Cardo&family=Dancing+Script&display=swap" rel="stylesheet">
<style>
:root{
  --stage:#8c8c8c;
  --paper:#f7f7f7;
  --paper-shade:#e6e6e6;
  --navy:#0d2f7a;
  --blue:#1747a8;
  --blue-light:#2f63c4;
  --steel:#8d8d8d;
  --ink:#4a4a4a;
  --label:#1e1e1e;
  --white:#ffffff;
}
*{box-sizing:border-box;margin:0;padding:0}
html,body{width:1200px;height:372px;overflow:hidden}
body{background:var(--stage);font-family:"Open Sans",sans-serif;color:var(--ink);position:relative}
.piece{position:absolute;background:linear-gradient(135deg,var(--white),var(--paper) 60%,var(--paper-shade));box-shadow:0 2px 5px rgba(0,0,0,.35);overflow:hidden}
.band{position:absolute;left:0;right:0;bottom:0;height:5px;background:linear-gradient(100deg,var(--navy),var(--blue-light) 74%,var(--white) 74.5%,var(--steel) 75.5%,#5c5c5c)}
.label{position:absolute;font-size:5.6px;color:var(--label);text-align:center}
.brand{font-family:"Open Sans",sans-serif;font-weight:700;color:var(--navy);letter-spacing:.12em;text-transform:uppercase;white-space:nowrap}
.brand-light{color:var(--white)}
.mark{display:inline-block;width:6px;height:6px;background:currentColor;margin-right:3px;vertical-align:middle}
.name{font-weight:700;color:var(--navy);font-size:4.6px}
.role{font-size:3.2px;color:#777}
.small{font-size:3px;line-height:1.45;color:#555}
.contact{font-size:3px;line-height:1.6;color:#555}
.contact svg{width:3px;height:3px;vertical-align:-0.4px;margin-right:2px;fill:var(--navy)}

/* intro */
.intro{position:absolute;left:28px;top:34px;width:118px;text-align:center;color:var(--white)}
.intro .brand{font-size:13px;color:var(--white)}
.intro .title{font-family:"Cardo",serif;font-size:9.5px;margin-top:10px}

/* cards */
.card{left:26px;width:129px;height:72px;border-radius:3px}
.card-01{top:98px}
.card-01 .brand{position:absolute;top:14px;left:0;right:0;text-align:center;font-size:9px}
.card-01 .tagline{position:absolute;top:25px;left:0;right:0;text-align:center;font-size:2.6px;letter-spacing:.08em;color:var(--navy)}
.card-01 .who{position:absolute;left:10px;top:37px;width:50px;text-align:right}
.card-01 .contact{position:absolute;left:69px;top:36px}
.card-02{top:184px}
.card-02 .brand{position:absolute;left:12px;top:31px;font-size:6.5px}
.card-02 .who{position:absolute;left:75px;top:15px}
.card-back{top:271px;height:72px;background:radial-gradient(circle at 30% 40%,var(--blue-light),var(--navy) 80%)}
.card-back .brand{position:absolute;left:10px;top:30px;font-size:7px}
.card-back .spec{position:absolute;left:61px;top:13px;color:var(--white)}
.card-back h4{font-size:4.3px;font-weight:700}
.card-back ul{font-size:3px;font-style:italic;line-height:1.5;padding-left:4px;margin-top:2px}

/* letterheads */
.letter-02{left:289px;top:45px;width:217px;height:278px}
.letter-02 .foot{position:absolute;left:96px;bottom:9px;font-size:3px;color:#555;line-height:1.6}
.letter-01{left:172px;top:64px;width:217px;height:281px}
.letter-01 .brand{position:absolute;left:15px;top:38px;font-size:6.5px}
.letter-01 .addr{position:absolute;left:161px;top:20px}
.letter-01 .body{position:absolute;left:15px;top:60px;width:186px;font-size:3.6px;line-height:1.5;color:#555}
.letter-01 .body p{margin-bottom:5px}
.letter-01 .lead{font-size:3.8px}
.letter-01 .sig{font-family:"Dancing Script",cursive;font-size:11px;color:#333;margin-top:4px;line-height:1}
.letter-01 .web{position:absolute;bottom:10px;left:0;right:0;text-align:center;font-size:3.2px;letter-spacing:.25em;color:#666;font-style:italic}

/* email signature */
.email{left:412px;top:61px;width:144px;height:69px}
.email .brand{position:absolute;left:20px;top:43px;font-size:6.5px}
.email .who{position:absolute;left:82px;top:14px}

/* envelope */
.envelope{left:319px;top:158px;width:234px;height:134px}
.envelope .flap{position:absolute;left:0;right:0;top:0;height:34px;background:linear-gradient(180deg,var(--blue-light),var(--navy));border-radius:0 0 0 0}
.envelope .flap .web{position:absolute;top:5px;left:0;right:0;text-align:center;color:var(--white);font-size:3px;letter-spacing:.2em;transform:rotate(180deg)}
.envelope .flap .brand{position:absolute;top:16px;left:0;right:0;text-align:center;font-size:5px;transform:rotate(180deg)}
.envelope .brand.front{position:absolute;left:14px;top:60px;font-size:6.5px}
.envelope .small{position:absolute;left:14px;top:73px}

/* folder */
.folder-back{left:575px;top:70px;width:171px;height:277px;background:radial-gradient(circle at 40% 30%,var(--blue-light),var(--navy) 85%);box-shadow:0 2px 5px rgba(0,0,0,.35)}
.folder-back .contact{position:absolute;left:10px;bottom:24px;color:var(--white);font-size:3.8px}
.folder-back .contact svg{fill:var(--white);width:3.6px;height:3.6px}
.folder-front{left:635px;top:32px;width:168px;height:290px}
.folder-front .brand{position:absolute;top:140px;left:0;right:0;text-align:center;font-size:9px}
.folder-inner{left:892px;top:48px;width:288px;height:266px;background:var(--paper)}
.folder-inner .fold{position:absolute;left:144px;top:0;bottom:0;width:1px;background:#cfcfcf}
.pocket{position:absolute;bottom:0;height:88px;width:143px;background:radial-gradient(circle at 50% 30%,var(--blue-light),var(--navy) 85%);border-radius:8px 8px 0 0}
.pocket-left{left:0}
.pocket-right{right:0}
.mini-card{position:absolute;right:38px;top:23px;width:62px;height:36px;background:var(--white);border-radius:2px;box-shadow:0 1px 3px rgba(0,0,0,.4)}
.mini-card .brand{position:absolute;left:5px;top:16px;font-size:3.4px}
.mini-card .who{position:absolute;left:34px;top:4px;font-size:2px;line-height:1.5;color:#555}
</style>
</head>
<body>

<svg width="0" height="0" style="position:absolute">
  <defs>
    <symbol id="i-phone" viewBox="0 0 10 10"><path d="M1 3a2 2 0 0 1 2-2h4a2 2 0 0 1 2 2v1H7V3H3v1H1z M2 5h6l1 4H1z"/></symbol>
    <symbol id="i-mobile" viewBox="0 0 10 10"><rect x="3" y="0.5" width="4" height="9" rx="0.8"/></symbol>
    <symbol id="i-mail" viewBox="0 0 10 10"><path d="M0 2h10v6H0z M0 2l5 3.5L10 2" /></symbol>
    <symbol id="i-web" viewBox="0 0 10 10"><circle cx="5" cy="5" r="4.5"/></symbol>
  </defs>
</svg>

<section class="intro">
  <div class="brand"><span class="mark"></span>Stonevia</div>
  <div class="title">Stationary Concepts</div>
</section>

<!-- business cards -->
<article class="piece card card-01">
  <div class="brand">Stonevia</div>
  <div class="tagline">TECHNOLOGY | ENGINEERING | CONSTRUCTION</div>
  <div class="who">
    <div class="name">Nolan Reed</div>
    <div class="role">Manager Director</div>
    <div class="small">C/248 Kelting Ridge Rd<br>Marrow Vale North, 2081, NSW</div>
  </div>
  <div class="contact">
    <div><svg><use href="#i-phone"/></svg>+61 2 9735 2194</div>
    <div><svg><use href="#i-mobile"/></svg>0412 000 000</div>
    <div><svg><use href="#i-mail"/></svg>info@stonevia.com.au</div>
    <div><svg><use href="#i-web"/></svg>www.stonevia.com.au</div>
  </div>
  <div class="band"></div>
</article>
<div class="label" style="left:26px;top:173px;width:129px">Front card_01</div>

<article class="piece card card-02">
  <div class="brand">Stonevia</div>
  <div class="who">
    <div class="name">Nolan Reed</div>
    <div class="role">Manager Director</div>
    <div class="small" style="margin-top:3px">C/248 Kelting Ridge Rd,<br>Marrow Vale North, 2081, NSW</div>
    <div class="contact" style="margin-top:2px">
      <div><svg><use href="#i-phone"/></svg>+61 2 9735 2194</div>
      <div><svg><use href="#i-mobile"/></svg>0412 000 000</div>
      <div><svg><use href="#i-mail"/></svg>info@stonevia.com.au</div>
      <div><svg><use href="#i-web"/></svg>www.stonevia.com.au</div>
    </div>
  </div>
  <div class="band"></div>
</article>
<div class="label" style="left:26px;top:259px;width:129px">Front card_02</div>

<article class="piece card card-back">
  <div class="brand brand-light">Stonevia</div>
  <div class="spec">
    <h4>Specialising in....</h4>
    <ul>
      <li>Landslip &amp; Flood Remediation</li>
      <li>Earth Retaining Structures</li>
      <li>Embankment Stabilisation</li>
      <li>Road &amp; Drainage Repairs</li>
      <li>Bridge Reconstruction</li>
      <li>Rockfall Protection</li>
      <li>Marine &amp; Foreshore Erosion Control</li>
      <li>Landfill Construction &amp; Rehabilitation</li>
    </ul>
  </div>
</article>
<div class="label" style="left:26px;top:346px;width:129px">Back card</div>

<!-- letterheads -->
<article class="piece letter-02">
  <div class="foot">C/248 Kelting Ridge Rd, Marrow Vale North, 2081, NSW<br><b>E :</b> info@stonevia.com.au &nbsp;<b>W :</b> www.stonevia.com.au</div>
  <div class="band"></div>
</article>
<div class="label" style="left:395px;top:329px">Letterhead_Option_02</div>

<article class="piece letter-01">
  <div class="brand">Stonevia</div>
  <div class="addr contact">
    <div>C/248 Kelting Ridge Rd,</div>
    <div>Marrow Vale North, 2081, NSW</div>
    <div><svg><use href="#i-phone"/></svg>+61 2 9735 2194</div>
    <div><svg><use href="#i-mobile"/></svg>0412 000 000</div>
    <div><svg><use href="#i-mail"/></svg>info@stonevia.com.au</div>
  </div>
  <div class="body">
    <p class="lead">Date</p>
    <p class="lead"><b>Recipient Name</b></p>
    <p>Company Name<br>Street Address<br>City, State, Zip</p>
    <p style="margin-top:12px">Lorem ipsum dolor sit amet, consectetuer adipiscing elit, sed diam nonummy nibh euismod tincidunt ut laoreet dolore magna aliquam erat volutpat. Ut wisi enim ad minim veniam, quis nostrud exerci tation ullamcorper suscipit lobortis nisl ut aliquip ex ea commodo consequat.</p>
    <p>Nulla facilisis at vero eros et accumsan et iusto odio dignissim qui blandit praesent luptatum zzril delenit augue duis dolore te feugait nulla facilisi. Nam liber tempor cum soluta nobis eleifend option congue nihil imperdiet.</p>
    <p>Legere me lius quod ii legunt saepius. Claritas est etiam processus dynamicus, qui sequitur mutationem consuetudium lectorum. Mirum est notare quam littera gothica.</p>
    <p>Legere me lius quod ii legunt saepius. Claritas est etiam processus dynamicus.</p>
    <p style="margin-top:10px">Sincerely,</p>
    <div class="sig">Signature</div>
    <div class="name" style="margin-left:15px">Nolan Reed</div>
    <div class="role" style="margin-left:15px">Manager Director</div>
  </div>
  <div class="web">www.stonevia.com.au</div>
  <div class="band"></div>
</article>
<div class="label" style="left:172px;top:351px;width:217px">Letterhead_Option_01</div>

<!-- email signature -->
<article class="piece email">
  <div class="brand">Stonevia</div>
  <div class="who">
    <div class="name">Nolan Reed</div>
    <div class="role">Manager Director</div>
    <div class="small" style="margin-top:3px">C/248 Kelting Ridge Rd,<br>Marrow Vale North, 2081, NSW</div>
    <div class="contact" style="margin-top:2px">
      <div><svg><use href="#i-phone"/></svg>+61 2 9735 2194</div>
      <div><svg><use href="#i-mobile"/></svg>0412 000 000</div>
      <div><svg><use href="#i-mail"/></svg>info@stonevia.com.au</div>
      <div><svg><use href="#i-web"/></svg>www.stonevia.com.au</div>
    </div>
  </div>
  <div class="band"></div>
</article>
<div class="label" style="left:412px;top:134px;width:144px">Email Signature</div>

<!-- envelope -->
<article class="piece envelope">
  <div class="flap">
    <div class="web">www.stonevia.com.au</div>
    <div class="brand brand-light">Stonevia</div>
  </div>
  <div class="brand front">Stonevia</div>
  <div class="small">C/248 Kelting Ridge Rd,<br>Marrow Vale North, 2081, NSW</div>
  <div class="band"></div>
</article>
<div class="label" style="left:512px;top:296px">Envelope_01</div>

<!-- folder -->
<article class="folder-back piece">
  <div class="contact">
    <div>C/248 Kelting Ridge Rd,</div>
    <div>Marrow Vale North, 2081, NSW</div>
    <div><svg><use href="#i-phone"/></svg>+61 2 9735 2194</div>
    <div><svg><use href="#i-mobile"/></svg>0412 000 000</div>
    <div><svg><use href="#i-mail"/></svg>info@stonevia.com.au</div>
  </div>
</article>
<div class="label" style="left:575px;top:350px;width:171px">Folder_Back</div>

<article class="piece folder-front">
  <div class="brand">Stonevia</div>
  <div class="band"></div>
</article>
<div class="label" style="left:755px;top:327px">Folder_Front</div>

<article class="piece folder-inner">
  <div class="fold"></div>
  <div class="pocket pocket-left"></div>
  <div class="pocket pocket-right">
    <div class="mini-card">
      <div class="brand">Stonevia</div>
      <div class="who"><b style="color:var(--navy)">Nolan Reed</b><br>Manager Director<br>C/248 Kelting Ridge<br>+61 2 9735 2194<br>0412 000 000<br>info@stonevia.com.au</div>
    </div>
  </div>
</article>
<div class="label" style="left:892px;top:319px;width:288px">Folder_Inner</div>

</body>
</html>
```